Thank You Card

I'm looking for a thank you card design using our logo and other graphics. We are an essential business and our employees (Electricians) have done an incredible job staying healthy and safe during the COVID-19 pandemic, I want to send each a thank you card.

```html
<!DOCTYPE html>
<html lang="en">
<head>
<meta charset="UTF-8">
<title>Thank You Cards – Essential Workers</title>
<link rel="stylesheet" href="https://fonts.googleapis.com/css2?family=Montserrat:wght@400;500;700;800&family=Great+Vibes&family=Mr+Dafoe&display=swap">
<style>
  :root {
    --canvas: #eef1ee;
    --card-white: #ffffff;
    --card-shade: #eeeeee;
    --gold: #e9b81f;
    --gold-deep: #d9a313;
    --rule-red: #e4343f;
    --brand-blue: #16308f;
    --brand-red: #e8112d;
    --ink: #1c1c1c;
    --hat-light: #f9c04a;
    --hat-dark: #e08a10;
  }
  * { box-sizing: border-box; margin: 0; padding: 0; }
  html, body {
    width: 1200px;
    height: 1192px;
    overflow: hidden;
    background: var(--canvas);
  }
  .canvas {
    position: relative;
    width: 1200px;
    height: 1192px;
  }
  .card {
    position: absolute;
    left: 50px;
    width: 1100px;
    height: 530px;
    border: 16px solid var(--gold);
    background: linear-gradient(160deg, var(--card-white) 0%, var(--card-shade) 45%, var(--card-white) 70%, var(--card-shade) 100%);
    box-shadow: 0 0 0 2px var(--gold-deep) inset;
  }
  .card::before {
    content: "";
    position: absolute;
    inset: 14px;
    border: 1px solid var(--rule-red);
    pointer-events: none;
  }
  .card--thanks { top: 50px; }
  .card--hero { top: 612px; }

  /* Front card */
  .brand-name {
    position: absolute;
    left: 120px;
    top: 70px;
    font-family: "Montserrat", sans-serif;
    font-weight: 800;
    font-size: 30px;
    letter-spacing: 1px;
    color: var(--brand-blue);
    text-transform: uppercase;
    display: flex;
    align-items: center;
    gap: 12px;
  }
  .brand-name .brand-mark {
    width: 22px;
    height: 22px;
    background: var(--brand-red);
  }
  .thanks-script {
    position: absolute;
    left: 110px;
    top: 130px;
    font-family: "Great Vibes", cursive;
    font-size: 230px;
    line-height: 1;
    color: var(--brand-red);
  }
  .thanks-caption {
    position: absolute;
    right: 150px;
    bottom: 70px;
    font-family: "Montserrat", sans-serif;
    font-weight: 700;
    font-size: 30px;
    letter-spacing: 1px;
    color: var(--brand-blue);
  }

  /* Message card */
  .hero-heading {
    position: absolute;
    left: 80px;
    top: 104px;
    display: flex;
    align-items: baseline;
    gap: 56px;
    font-family: "Montserrat", sans-serif;
    font-weight: 800;
    line-height: 1;
  }
  .hero-heading__lead { font-size: 64px; color: var(--brand-blue); }
  .hero-heading__word {
    position: relative;
    font-size: 76px;
    color: var(--brand-red);
  }
  .hero-heading__art {
    position: absolute;
    left: -18px;
    top: -88px;
    width: 120px;
    height: 80px;
    border-radius: 12px;
    background: linear-gradient(135deg, var(--hat-light), var(--hat-dark));
  }
  .message {
    position: absolute;
    left: 80px;
    top: 200px;
    width: 920px;
    font-family: "Montserrat", sans-serif;
  }
  .message__main {
    font-size: 30px;
    line-height: 1.35;
    color: var(--brand-blue);
  }
  .message__main .accent { color: var(--brand-red); }
  .message__note {
    margin-top: 22px;
    width: 620px;
    font-size: 21px;
    line-height: 1.45;
    color: var(--brand-blue);
  }
  .message__note .accent { color: var(--brand-red); }
  .sign-off {
    position: absolute;
    right: 90px;
    bottom: 44px;
    text-align: left;
  }
  .sign-off__line {
    font-family: "Montserrat", sans-serif;
    font-size: 24px;
    color: var(--brand-red);
  }
  .sign-off__name {
    font-family: "Mr Dafoe", cursive;
    font-size: 48px;
    color: var(--ink);
    margin-top: 4px;
  }
</style>
</head>
<body>
<main class="canvas">
  <section class="card card--thanks">
    <div class="brand-name"><span class="brand-mark"></span>Brightline Electric Co.</div>
    <div class="thanks-script">thank you</div>
    <div class="thanks-caption">Essential Worker 2020</div>
  </section>

  <section class="card card--hero">
    <h1 class="hero-heading">
      <span class="hero-heading__lead">YOU ARE A</span>
      <span class="hero-heading__word">HERO<span class="hero-heading__art" role="img" aria-label="Illustration of an orange safety hard hat with brim"></span></span>
    </h1>
    <div class="message">
      <p class="message__main">You have done an incredible job providing essential services <span class="accent">during the COVID-19 pandemic.</span></p>
      <p class="message__note"><span class="accent">Stay safe and healthy,</span> if there is anything I can do for you please let me know.</p>
    </div>
    <div class="sign-off">
      <p class="sign-off__line">With gratitude,</p>
      <p class="sign-off__name">Daniel Hartley</p>
    </div>
  </section>
</main>
</body>
</html>
```